Wordpress Design for my Consulting Company

We want a WordPress site created for our new business. We have created a mock-up of the content we want on the site at https://marcusdellow.example-sites.com/website-5

We are not attached to any of the pictures and just put stock stuff from wix's editor, which we don't have rights to use outside of wix.

We are NOT looking to just port this site to WordPress, we are looking for some creative ways to display the content in a more professional artistic sense.

I have included several logo files and a text file with the colors and Fonts used in the logo. We are not looking to change the logo or the colors used in the logo.

The Schedule appointment links to a page that embeds a bookingnest.example.com calendar. https://bookingnest.example.com/marcus-dellow/brightvale

The final website domain will be enterprisebrightvale.example

Enterprise brightvale is a consulting company that works directly with the business owners and leaders of small businesses between 50-200 employees. We help companies make sure they have the right technology to meet their strategic goals. We are the anti-"Computer Guy" and we focus on business outcomes NOT cool technology gadgets.

The final design should communicate business growth and success.

Target Market(s)

Business Owners of companies with 50-200 employees

Coding

Coded - Design and coding required

Number of Pages Required

1 page

Font styles to use
Serif
Other font styles liked:
• Trajan Pro Bold, Open Sans

Requirements
Must have
• Should focus on consulting rather than technology.
• Should show the customer as the hero and we are just their guide.
• Must use the logo provided and the colors and fonts in the text file provided. Any other colors and fonts must be complementary.
• The design should scale for all devices computer, iPad, or phone
Should not have
• Should not focus on technology, we are the anti-"Computer Guy" and we focus on business outcomes NOT cool technology gadgets.

```html
<!DOCTYPE html>
<html lang="en">
<head>
<meta charset="utf-8">
<title>Brightvale – Technology Advisors</title>
<link href="https://fonts.googleapis.com/css2?family=Roboto:ital,wght@0,300;0,400;0,500;0,700;1,400;1,500&display=swap" rel="stylesheet">
<style>
:root{
  --slate:#4b575c;
  --slate-dark:#3f4a4f;
  --orange:#c9744a;
  --ink:#3a3f42;
  --grey:#8a8f92;
  --light:#f1f1f1;
  --line:#d9d9d9;
  --white:#ffffff;
}
*{box-sizing:border-box;margin:0;padding:0}
html,body{width:1200px;height:3377px;overflow:hidden}
body{position:relative;font-family:"Roboto",Arial,sans-serif;color:var(--ink);background:var(--white)}
.abs{position:absolute}
.photo{position:absolute}

/* hero */
.hero-photo{left:0;top:0;width:574px;height:603px;background:linear-gradient(180deg,#dfe6ea 0%,#b9c4cb 45%,#6f6660 75%,#4a4039 100%)}
.hero-panel{left:574px;top:0;width:626px;height:603px;background:linear-gradient(160deg,#56636a,var(--slate) 60%,#435055)}
.brand{left:150px;top:40px;display:flex;align-items:center;gap:10px;font-weight:700;font-size:20px;letter-spacing:2px;color:var(--ink)}
.brand i{display:block;width:26px;height:26px;border-radius:50%;background:var(--orange)}
.nav{left:705px;top:38px;display:flex;gap:26px;font-size:12px;color:var(--white);text-transform:uppercase}
.hero-tab{left:490px;top:162px;width:62px;height:279px;background:var(--orange)}
.hero-tab span{position:absolute;left:50%;top:50%;transform:translate(-50%,-50%) rotate(-90deg);font-weight:700;font-size:32px;letter-spacing:3px;color:var(--white)}
.hero-box{left:552px;top:162px;width:486px;height:279px;border:2px solid var(--white)}
.hero-kicker{left:603px;top:208px;font-weight:300;font-size:27px;color:var(--white)}
.hero-title{left:603px;top:236px;font-weight:700;font-size:40px;color:var(--white)}
.hero-text{left:605px;top:288px;width:380px;font-size:18px;line-height:23px;color:#e6e9ea}
.btn-outline{left:608px;top:360px;width:167px;height:33px;border:1.5px solid var(--white);color:var(--white);font-size:11px;display:flex;align-items:center;justify-content:center;text-transform:uppercase}

/* about */
.rule{background:var(--grey)}
.about-label{left:84px;top:760px;transform:rotate(-90deg);font-weight:300;font-size:30px;letter-spacing:4px;color:var(--ink)}
.about-lead{left:160px;top:668px;font-weight:300;font-size:26px}
.about-title{left:160px;top:694px;font-weight:700;font-size:38px;color:var(--orange)}
.about-intro{left:160px;top:738px;width:480px;font-style:italic;font-size:13px;line-height:18px;color:var(--ink)}
.about-body{left:160px;width:475px;font-size:12px;line-height:17px;color:var(--grey)}
.about-photo{left:662px;top:675px;width:376px;height:248px;background:linear-gradient(135deg,#e8ecef,#9fa9b3 55%,#49546a)}

/* four steps */
.team-photo{left:0;top:979px;width:597px;height:455px;background:linear-gradient(180deg,#c9cfd4,#7d848c 50%,#2f3338)}
.play{left:268px;top:1153px}
.steps-panel{left:597px;top:979px;width:603px;height:455px;background:linear-gradient(120deg,#f3f3f3,#e4e5e6)}
.steps-brand{left:840px;top:1036px;display:flex;align-items:center;gap:8px;font-weight:700;font-size:15px;letter-spacing:2px}
.steps-brand i{display:block;width:22px;height:22px;border-radius:50%;background:var(--orange)}
.steps-title{left:597px;width:603px;top:1096px;text-align:center;font-weight:700;font-size:29px;color:var(--ink)}
.steps-sub{left:640px;width:520px;top:1134px;text-align:center;font-size:19px;line-height:24px;text-transform:uppercase;color:var(--ink)}
.steps-text{left:645px;width:510px;top:1186px;text-align:center;font-size:12px;line-height:17px;color:var(--grey)}
.step{top:1278px;width:140px;text-align:center}
.step svg{display:block;margin:0 auto 10px}
.step h4{font-size:13px;font-weight:700;color:var(--ink);margin-bottom:4px}
.step p{font-size:11px;line-height:15px;color:var(--grey)}

/* meeting */
.band{left:0;width:1200px;background:var(--orange);color:var(--white);display:flex;align-items:center;justify-content:center}
.meeting-band{top:1434px;height:90px;font-weight:700;font-size:33px}
.day-title{left:0;width:1200px;top:1560px;text-align:center;font-weight:700;font-size:25px;color:#55595c}
.today{left:178px;top:1606px;font-weight:700;font-size:12px;color:var(--ink)}
.day{width:110px;height:110px;border-radius:50%;border:7px solid var(--orange);background:var(--white);top:1633px;display:flex;flex-direction:column;align-items:center;justify-content:center;box-shadow:inset 0 0 0 3px #fff,inset 0 0 0 5px #c9c9c9}
.day b{font-size:14px;color:var(--ink)}
.day span{font-size:11px;color:var(--grey)}
.card{top:1794px;width:276px;height:126px;display:flex;align-items:center;justify-content:center;text-align:center;color:var(--white);font-size:17px;line-height:21px;text-transform:uppercase}
.card.orange{background:var(--orange)}
.card.slate{background:var(--slate)}
.arrow{top:1841px;width:32px;height:32px;border-radius:50%;background:#e3e3e3;display:flex;align-items:center;justify-content:center}

/* clients */
.clients-left{left:0;top:1981px;width:563px;height:203px;background:var(--slate)}
.clients-right{left:563px;top:1981px;width:637px;height:203px;background:var(--orange)}
.clients-icon{left:165px;top:2041px}
.clients-title{left:218px;top:2043px;font-weight:700;font-size:15px;color:var(--white)}
.clients-text{left:218px;top:2070px;width:300px;font-size:12px;line-height:17px;color:#dfe3e4}
.avatar{left:590px;top:2031px;width:80px;height:80px;border-radius:50%;border:3px solid var(--white);background:linear-gradient(180deg,#d8d2cc,#5f6a78)}
.quote{left:690px;top:2022px;width:480px;font-style:italic;font-size:13px;line-height:19px;color:var(--white)}
.quote-by{left:690px;top:2138px;font-style:italic;font-weight:700;font-size:13px;color:var(--white)}
.dot{left:1168px;width:7px;height:7px;border-radius:50%;background:var(--white)}

/* computer guys */
.guys-back{left:0;top:2243px;width:500px;height:527px;background:linear-gradient(135deg,#ececec,#dcdcdc)}
.guys-frame{left:162px;top:2300px;width:405px;height:413px;background:var(--white);box-shadow:0 2px 10px rgba(0,0,0,.08)}
.guys-photo{left:180px;top:2319px;width:367px;height:376px;background:linear-gradient(160deg,#e7e4de,#a9b3bd 50%,#485b6d)}
.guys-lead{left:599px;top:2296px;font-weight:300;font-size:29px;color:var(--ink)}
.guys-title{left:599px;top:2326px;font-weight:700;font-size:31px;color:var(--ink)}
.tick{left:599px;width:400px;display:flex;gap:14px;font-size:14px;line-height:20px;color:#6f7476}
.tick svg{flex:none;margin-top:-1px}

/* info bar */
.info-bar{left:0;top:2837px;width:1200px;height:83px;background:var(--light)}
.info{top:2856px;display:flex;gap:14px;align-items:flex-start}
.info b{display:block;font-size:12px;color:var(--ink)}
.info span{display:block;font-size:12px;line-height:16px;color:var(--ink)}

/* contact */
.contact-left{left:0;top:2920px;width:608px;height:408px;background:var(--slate)}
.contact-photo{left:608px;top:2920px;width:592px;height:408px;background:linear-gradient(150deg,#e9ecef,#b4b8bb 50%,#6f5a55)}
.contact-label{left:40px;top:3050px;transform:rotate(-90deg);font-weight:300;font-size:30px;letter-spacing:4px;color:var(--white)}
.field{left:160px;width:421px;height:36px;border:1px solid #8b979c;background:#56636a;color:#d7dcde;font-size:11px;padding:0 12px;display:flex;align-items:center}
.field.msg{align-items:flex-start;padding-top:12px;height:126px}
.btn-submit{left:160px;top:3255px;width:110px;height:32px;background:var(--orange);color:var(--white);font-weight:700;font-size:12px;display:flex;align-items:center;justify-content:center}

/* footer */
.footer{left:0;top:3328px;width:1200px;height:49px;background:var(--orange);color:var(--white);font-size:11px}
.copy{left:162px;top:18px}
.connect{left:840px;top:15px;font-size:13px;font-weight:500}
.social{top:13px;width:24px;height:24px;border-radius:50%;border:1.5px solid var(--white)}
</style>
</head>
<body>

<!-- hero -->
<div class="photo hero-photo" role="img" aria-label="Businessman with briefcase standing on a wooden ledge above a city skyline"></div>
<div class="abs hero-panel"></div>
<div class="abs brand"><i></i>BRIGHTVALE</div>
<nav class="abs nav"><span>Home</span><span>About Us</span><span>Services</span><span>Schedule Appointment</span></nav>
<div class="abs hero-box"></div>
<div class="abs hero-tab"><span>BRIGHTVALE</span></div>
<div class="abs hero-kicker">TECHNOLOGY ADVISORS</div>
<div class="abs hero-title">THAT "GET" BUSINESS.</div>
<p class="abs hero-text">We help you leverage technology to create a competitive advantage.</p>
<div class="abs btn-outline">Schedule Appointment</div>
<svg class="abs" style="left:591px;top:556px" width="16" height="24" viewBox="0 0 16 24"><rect x="1" y="1" width="14" height="22" rx="7" fill="none" stroke="#fff" stroke-width="1.5"/><rect x="7" y="5" width="2" height="6" rx="1" fill="#fff"/></svg>

<!-- about -->
<div class="abs rule" style="left:387px;top:603px;width:1.5px;height:86px"></div>
<div class="abs" style="left:383px;top:686px;width:9px;height:9px;border-radius:50%;background:var(--grey)"></div>
<div class="abs rule" style="left:40px;top:630px;width:348px;height:1.5px"></div>
<div class="abs rule" style="left:40px;top:630px;width:1.5px;height:40px"></div>
<div class="abs about-label">ABOUT</div>
<div class="abs rule" style="left:0;top:833px;width:140px;height:1.5px"></div>
<div class="abs about-lead">Helping associates to</div>
<div class="abs about-title">ACHIEVE SUCCESS</div>
<p class="abs about-intro">Lorem Ipsum is simply dummy text of the printing and typesetting industry. Lorem Ipsum has been the industry's standard dummy...</p>
<p class="abs about-body" style="top:783px">Lorem Ipsum is simply dummy text of the printing and typesetting industry. Lorem Ipsum has been the industry's standard dummy text ever since the 1500s, when an unknown printer took galley of type and scrambled it to make a type specimen book. It has survived not only five PageMaker including versions of Lorem Ipsum.</p>
<p class="abs about-body" style="top:856px">Lorem Ipsum is simply dummy text of the printing and typesetting industry. Lorem Ipsum has been the industry's standard dummy text ever since the 1500s, when an unknown printer took galley of type and scrambled it to make a type specimen book. It has survived not only five PageMaker including versions of Lorem Ipsum.</p>
<div class="photo about-photo" role="img" aria-label="Two colleagues reviewing documents at a desk"></div>

<!-- four steps -->
<div class="photo team-photo" role="img" aria-label="Group of business professionals standing together in an office"></div>
<svg class="abs play" width="80" height="80" viewBox="0 0 80 80"><circle cx="40" cy="40" r="36" fill="rgba(255,255,255,.25)" stroke="#fff" stroke-width="3"/><path d="M32 26 L56 40 L32 54 Z" fill="#fff"/></svg>
<div class="abs steps-panel"></div>
<div class="abs steps-brand"><i></i>BRIGHTVALE</div>
<h2 class="abs steps-title">THE FOUR STEPS</h2>
<p class="abs steps-sub">To aligning technology to your business strategy!</p>
<p class="abs steps-text">Lorem Ipsum is simply dummy text of the printing and typesetting industry. Lorem Ipsum has galley of type and scrambled it to make a type specimen book. PageMaker including</p>

<div class="abs step" style="left:605px">
  <svg width="48" height="48" viewBox="0 0 48 48"><circle cx="19" cy="19" r="13" fill="none" stroke="#3a3f42" stroke-width="4"/><path d="M29 29 L43 43" stroke="#3a3f42" stroke-width="6" stroke-linecap="round"/></svg>
  <h4>DISCOVER</h4><p>Lorem Ipsum is simply printing and typesetting industry been...</p>
</div>
<div class="abs step" style="left:756px">
  <svg width="48" height="48" viewBox="0 0 48 48"><rect x="16" y="4" width="26" height="20" fill="none" stroke="#3a3f42" stroke-width="3"/><path d="M21 11h16M21 17h10" stroke="#3a3f42" stroke-width="2"/><circle cx="10" cy="14" r="4" fill="#3a3f42"/><path d="M5 22h10v12H5zM7 34v10M13 34v10M29 24v20" stroke="#3a3f42" stroke-width="3" fill="#3a3f42"/></svg>
  <h4>PRIORITIZE</h4><p>Lorem Ipsum is simply printing and typesetting industry been...</p>
</div>
<div class="abs step" style="left:907px">
  <svg width="48" height="48" viewBox="0 0 48 48"><circle cx="24" cy="24" r="13" fill="none" stroke="#3a3f42" stroke-width="7" stroke-dasharray="6 4.2"/><circle cx="24" cy="24" r="10" fill="#3a3f42"/><circle cx="24" cy="24" r="4" fill="#ececec"/></svg>
  <h4>IMPLEMENT</h4><p>Lorem Ipsum is simply printing and typesetting industry been...</p>
</div>
<div class="abs step" style="left:1056px">
  <svg width="48" height="48" viewBox="0 0 48 48"><circle cx="24" cy="20" r="11" fill="none" stroke="#3a3f42" stroke-width="6" stroke-dasharray="5 3.6"/><circle cx="24" cy="20" r="5" fill="#3a3f42"/><path d="M20 32 L24 44 L28 32" fill="#3a3f42"/></svg>
  <h4>MAINTAIN</h4><p>Lorem Ipsum is simply printing and typesetting industry been...</p>
</div>

<!-- meeting -->
<div class="abs band meeting-band">BRIGHTVALE MEETING</div>
<h2 class="abs day-title">SELECT A DAY</h2>
<div class="abs today">~ TODAY ~</div>
<div class="abs day" style="left:161px"><b>MON</b><span>NOV 26</span></div>
<div class="abs day" style="left:287px"><b>TUE</b><span>NOV 27</span></div>
<div class="abs day" style="left:413px"><b>WED</b><span>NOV 28</span></div>
<div class="abs day" style="left:539px"><b>THU</b><span>NOV 28</span></div>
<div class="abs day" style="left:665px"><b>FRI</b><span>NOV 28</span></div>
<div class="abs day" style="left:791px"><b>SAT</b><span>NOV 28</span></div>
<div class="abs day" style="left:927px"><b>SUN</b><span>NOV 28</span></div>

<div class="abs arrow" style="left:94px"><svg width="10" height="12" viewBox="0 0 10 12"><path d="M7 1 L2 6 L7 11" fill="none" stroke="#777" stroke-width="2"/></svg></div>
<div class="abs card orange" style="left:162px">We get...<br>Eliminating bottlenecks</div>
<div class="abs card slate" style="left:462px">We get...<br>Standardizing customer<br>experience</div>
<div class="abs card slate" style="left:762px">We get...<br>Preparing for disruption</div>
<div class="abs arrow" style="left:1069px"><svg width="10" height="12" viewBox="0 0 10 12"><path d="M3 1 L8 6 L3 11" fill="none" stroke="#777" stroke-width="2"/></svg></div>

<!-- clients -->
<div class="abs clients-left"></div>
<div class="abs clients-right"></div>
<svg class="abs clients-icon" width="38" height="38" viewBox="0 0 38 38"><rect x="4" y="6" width="22" height="28" fill="none" stroke="#fff" stroke-width="2.5"/><path d="M9 14h12M9 20h12M9 26h8" stroke="#fff" stroke-width="2"/><path d="M24 26 L34 10 L37 12 L27 28 Z" fill="#fff"/></svg>
<div class="abs clients-title">WHAT CLIENTS SAY</div>
<p class="abs clients-text">Lorem Ipsum is simply dummy text of the printing and typesetting industry. Lorem Ipsum has been...</p>
<div class="abs avatar" role="img" aria-label="Portrait of a client"></div>
<p class="abs quote">“ I knew I was behind, I just didn't know by how much. We had years of band-aided solutions and Brightvale helped us stabilize our environment and position ourselves to compete in the quickly changing world of copy and print<br>-Dale Whitford, Print Nook ”</p>
<div class="abs quote-by">- Owen Carraway</div>
<div class="abs dot" style="top:2064px"></div>
<div class="abs dot" style="top:2077px;background:transparent;border:1px solid #fff"></div>
<div class="abs dot" style="top:2090px"></div>

<!-- computer guys -->
<div class="abs guys-back"></div>
<div class="abs guys-frame"></div>
<div class="photo guys-photo" role="img" aria-label="Smiling man working on a laptop"></div>
<div class="abs guys-lead">ARE YOU TIRED</div>
<div class="abs guys-title">OF "COMPUTER GUYS" THAT...</div>
<div class="abs tick" style="top:2383px"><svg width="24" height="24" viewBox="0 0 24 24"><circle cx="12" cy="12" r="12" fill="var(--orange)"/><path d="M6.5 12.5 L10.5 16 L17.5 8.5" fill="none" stroke="#fff" stroke-width="2.5"/></svg><span>Don't want to be involved in business strategy.</span></div>
<div class="abs tick" style="top:2424px"><svg width="24" height="24" viewBox="0 0 24 24"><circle cx="12" cy="12" r="12" fill="var(--orange)"/><path d="M6.5 12.5 L10.5 16 L17.5 8.5" fill="none" stroke="#fff" stroke-width="2.5"/></svg><span>Give you the excuse, "You never asked."?</span></div>
<div class="abs tick" style="top:2469px"><svg width="24" height="24" viewBox="0 0 24 24"><circle cx="12" cy="12" r="12" fill="var(--orange)"/><path d="M6.5 12.5 L10.5 16 L17.5 8.5" fill="none" stroke="#fff" stroke-width="2.5"/></svg><span>Say "No!" but do not give options on how to achieve your business outcome.</span></div>
<div class="abs tick" style="top:2527px"><svg width="24" height="24" viewBox="0 0 24 24"><circle cx="12" cy="12" r="12" fill="var(--orange)"/><path d="M6.5 12.5 L10.5 16 L17.5 8.5" fill="none" stroke="#fff" stroke-width="2.5"/></svg><span>Can't explain how a technology will create business value, but insist it is necessary.</span></div>
<div class="abs tick" style="top:2586px"><svg width="24" height="24" viewBox="0 0 24 24"><circle cx="12" cy="12" r="12" fill="var(--orange)"/><path d="M6.5 12.5 L10.5 16 L17.5 8.5" fill="none" stroke="#fff" stroke-width="2.5"/></svg><span>Recommend technology when a simple process or policy change would have the same effect.</span></div>
<div class="abs tick" style="top:2647px"><svg width="24" height="24" viewBox="0 0 24 24"><circle cx="12" cy="12" r="12" fill="var(--orange)"/><path d="M6.5 12.5 L10.5 16 L17.5 8.5" fill="none" stroke="#fff" stroke-width="2.5"/></svg><span>Suggest expensive solutions that are just thrown away, soon after they are deployed.</span></div>

<!-- info bar -->
<div class="abs info-bar"></div>
<div class="abs info" style="left:160px">
  <svg width="50" height="44" viewBox="0 0 50 44"><path d="M4 14 Q25 0 46 14 L42 20 L34 16 L34 11 Q25 8 16 11 L16 16 L8 20 Z" fill="none" stroke="var(--orange)" stroke-width="2.5"/><rect x="10" y="20" width="30" height="20" rx="3" fill="none" stroke="var(--orange)" stroke-width="2.5"/><circle cx="25" cy="30" r="5" fill="none" stroke="var(--orange)" stroke-width="2.5"/></svg>
  <div><b>CALL TO US</b><span>(555) 014-2276</span></div>
</div>
<div class="abs info" style="left:463px">
  <svg width="58" height="40" viewBox="0 0 58 40"><rect x="2" y="4" width="54" height="34" fill="none" stroke="var(--orange)" stroke-width="2.5"/><path d="M2 4 L29 24 L56 4M2 38 L22 19M56 38 L36 19" fill="none" stroke="var(--orange)" stroke-width="2.5"/></svg>
  <div><b>EMAIL</b><span>mdellow@enterprisebrightvale.example</span></div>
</div>
<div class="abs info" style="left:826px">
  <svg width="36" height="46" viewBox="0 0 36 46"><path d="M18 44 C8 30 4 24 4 17 A14 14 0 0 1 32 17 C32 24 28 30 18 44 Z" fill="none" stroke="var(--orange)" stroke-width="2.5"/><circle cx="18" cy="17" r="5" fill="none" stroke="var(--orange)" stroke-width="2.5"/></svg>
  <div><b>VISIT US</b><span>1480 Harlow Ridge Parkway South,<br>Marlow Springs, TX 75012</span></div>
</div>

<!-- contact -->
<div class="abs contact-left"></div>
<div class="photo contact-photo" role="img" aria-label="Business meeting with colleagues around a table"></div>
<div class="abs contact-label">CONTACT</div>
<div class="abs" style="left:0;top:3163px;width:136px;height:1.5px;background:#c4cacc"></div>
<div class="abs field" style="top:2970px">&#128100;&nbsp; Name:</div>
<div class="abs field" style="top:3017px">&#9993;&nbsp; Email:</div>
<div class="abs field" style="top:3066px">&#9743;&nbsp; Phone Number:</div>
<div class="abs field msg" style="top:3116px">&#9998;&nbsp; Message:</div>
<div class="abs btn-submit">SUBMIT NOW</div>

<!-- footer -->
<footer class="abs footer">
  <div class="abs copy">Copyright 2018 enterprisebrightvale.example</div>
  <div class="abs connect">Connect with us:</div>
  <div class="abs social" style="left:950px"></div>
  <div class="abs social" style="left:983px"></div>
  <div class="abs social" style="left:1016px"></div>
</footer>

</body>
</html>
```